Waschkarten-Design für Tankstelle gesucht
Zielgruppe
Unsere Tankstelle hat in eine neue Waschanlage investiert. Die Alten Waschkarten gefallen nicht mehr, und sind auch mit der Programmstruktur nicht mehr kompatibel. Siehe Anhang.
Waschkunden in der Portalwaschanlage jeglichen Alters und Geschlechts.
Aufgabenstellung
Wertigkeit der einzelnen Waschprogramme muss erkennbar sein. Beschriftung z. B. Mehrfachwäschen 3er 5er 10er bzw. Wertkarten der Preis soll veränderbar sein, so das die Karten jederzeit angepasst werden können. Auch sollte der Programm-Name von uns selbst geändert werden können. Die Einschiebe Richtung muss klar erkennbar sein.
Das Design muss im Check-Kartenformat sein. Achtung abgerundete Ecken mit ca. r=2 mm
Anbei ein Bild von unserer Neuen Waschanlage

```html
<!DOCTYPE html>
<html lang="de">
<head>
<meta charset="utf-8">
<title>Lindner – Wäsche A</title>
<link rel="stylesheet" href="https://fonts.googleapis.com/css2?family=Baloo+2:wght@700;800&family=Arimo&display=swap">
<style>
  :root {
    --card-blue: #1a8bca;
    --title-yellow: #f7c600;
    --sub-yellow: #f6e08c;
    --text-light: #dce9f2;
    --address-grey: #d5e4ee;
    --name-ink: #0d1b33;
    --curve-salmon: #e9b39c;
    --foam-deep: #1a4b93;
    --foam-light: #c9f3ec;
    --stage: #eef0f1;
  }
  html, body {
    margin: 0;
    width: 1200px;
    height: 728px;
    overflow: hidden;
    background: var(--stage);
  }
  .wash-card {
    position: relative;
    width: 1200px;
    height: 728px;
    background: var(--card-blue);
    border-radius: 18px;
    overflow: hidden;
    font-family: "Baloo 2", "Trebuchet MS", sans-serif;
  }
  .program-title {
    position: absolute;
    left: 62px;
    top: 62px;
    margin: 0;
    font-size: 66px;
    font-weight: 800;
    line-height: 1;
    color: var(--title-yellow);
  }
  .program-level {
    position: absolute;
    left: 62px;
    top: 190px;
    margin: 0;
    font-size: 48px;
    font-weight: 800;
    line-height: 1;
    color: var(--sub-yellow);
  }
  .program-detail {
    position: absolute;
    left: 62px;
    top: 256px;
    margin: 0;
    font-size: 38px;
    font-weight: 700;
    line-height: 1;
    color: var(--text-light);
  }
  .station-name {
    position: absolute;
    left: 795px;
    top: 118px;
    margin: 0;
    font-size: 76px;
    font-weight: 800;
    line-height: 1;
    color: var(--name-ink);
  }
  .station-address {
    position: absolute;
    left: 780px;
    top: 262px;
    margin: 0;
    font-family: "Arimo", Arial, sans-serif;
    font-size: 26px;
    line-height: 32px;
    color: var(--address-grey);
  }
  .insert-arrow {
    position: absolute;
    left: 52px;
    top: 318px;
    width: 520px;
    height: 128px;
  }
  .foam-scene {
    position: absolute;
    left: 0;
    bottom: 0;
    width: 1200px;
    height: 262px;
  }
  .curved-slogan {
    position: absolute;
    left: 0;
    top: 0;
    width: 1200px;
    height: 728px;
  }
</style>
</head>
<body>
  <main class="wash-card">
    <h1 class="program-title">Lindner - Wasche A</h1>
    <p class="program-level">BASIS - WASCHE</p>
    <p class="program-detail">Hochdruck - Wasche</p>

    <p class="station-name">Lindner</p>
    <p class="station-address">Talweg 7. 12345 Musterau<br>Tel. 01234 - 56 78 90</p>

    <svg class="insert-arrow" viewBox="0 0 520 128" aria-label="Einschubrichtung">
      <defs>
        <linearGradient id="arrowFade" x1="0" x2="1" y1="0" y2="0">
          <stop offset="0" stop-color="#d7e5ee"/>
          <stop offset="0.55" stop-color="#8fc0e0" stop-opacity="0.7"/>
          <stop offset="1" stop-color="#1a8bca" stop-opacity="0"/>
        </linearGradient>
      </defs>
      <polygon points="0,64 112,0 112,40 520,40 520,88 112,88 112,128" fill="url(#arrowFade)"/>
    </svg>

    <svg class="foam-scene" viewBox="0 0 1200 262" role="img" aria-label="Illustration: Sportwagen in Schaumblasen">
      <defs>
        <linearGradient id="foamTone" x1="0" x2="0" y1="0" y2="1">
          <stop offset="0" stop-color="var(--card-blue)"/>
          <stop offset="0.3" stop-color="var(--foam-deep)"/>
          <stop offset="1" stop-color="var(--foam-light)"/>
        </linearGradient>
      </defs>
      <rect x="0" y="0" width="1200" height="262" fill="url(#foamTone)"/>
    </svg>

    <svg class="curved-slogan" viewBox="0 0 1200 728" aria-hidden="false">
      <path id="sloganCurve" d="M184 488 C 360 520, 480 590, 620 540 S 800 380, 900 420 S 1080 500, 1150 540" fill="none"/>
      <text font-family="'Baloo 2', 'Trebuchet MS', sans-serif" font-weight="800" font-size="56" fill="var(--curve-salmon)">
        <textPath href="#sloganCurve" textLength="1000" lengthAdjust="spacing">Hier Waschenkeine Kratzbursten</textPath>
      </text>
    </svg>
  </main>
</body>
</html>
```